New more attractive design for an old tired look that is high tech but inviting

Need a more modern eye catching design. We are and I/T and MSP and we need a new look. Need a call to action on each page. Needs to be in WordPress. Existing site is quorbelna.com. Needs to work on phones and tablets. The default home page should present us as an MSP/MSSP and direct the viewer to our services we offer.
Updates

Current deadline assigned at project inception has passed before project started

Need extra days to review

Target Market(s)

Our target market is other businesses. We do not target residential customers.

Industry/Entity Type

Business to Business oriented

Coding

Coded - Design and coding required

Number of Pages Required

5+ page

Font styles to use
Sans Serif

Requirements
Must have
• Must have a current relevant design with a call to action on each page.
Nice to have
• Dark background high tech look with people to make it attractive

```html
<!DOCTYPE html>
<html lang="en">
<head>
<meta charset="utf-8">
<title>Corvane Systems – Managed IT & Data Center Services</title>
<link href="https://fonts.googleapis.com/css2?family=Poppins:wght@300;400;500;600&display=swap" rel="stylesheet">
<style>
:root{
  --red:#d7232f;
  --ink:#222;
  --ink-soft:#555;
  --teal-ink:#0f2c2c;
  --dark:#333;
  --line:#c9c9c9;
  --icon-bg:#e6f0f8;
  --white:#fff;
  --page-tint:#f6f5f5;
}
*{box-sizing:border-box;margin:0;padding:0}
html,body{width:1200px;height:3162px;overflow:hidden}
body{font-family:'Poppins',sans-serif;color:var(--ink);background:var(--white);position:relative}
a{color:inherit;text-decoration:none}
.abs{position:absolute}

.topbar{position:absolute;top:0;left:0;width:1200px;height:44px;background:var(--dark);color:var(--white);font-size:13px}
.topbar-red{position:absolute;left:0;top:0;width:595px;height:44px;background:var(--red);clip-path:polygon(0 0,100% 0,565px 100%,0 100%)}
.topbar .addr{position:absolute;left:114px;top:13px;display:flex;align-items:center;gap:8px}
.topbar .contact{position:absolute;right:112px;top:12px;display:flex;align-items:center;gap:8px}
.dot{width:18px;height:18px;border-radius:50%;background:var(--white);display:inline-block}

.header{position:absolute;top:44px;left:0;width:1200px;height:129px;background:var(--white)}
.logo{position:absolute;display:flex;align-items:center;gap:8px;font-weight:600;font-size:28px;letter-spacing:-0.5px;white-space:nowrap}
.logo .sq{width:12px;height:12px;background:var(--red)}
.nav{position:absolute;left:460px;top:58px;display:flex;gap:43px;font-size:15px;color:#333}
.nav .active{color:var(--red);font-weight:600}
.quote-btn{position:absolute;left:902px;top:46px;width:188px;height:47px;border:2px solid var(--red);display:flex;align-items:center;justify-content:center;font-size:15px;color:#333}

.hero{position:absolute;top:173px;left:0;width:1200px;height:604px;background:linear-gradient(100deg,#0e2436 0%,#1a3a55 45%,#254b6b 70%,#12283c 100%)}
.hero h1{position:absolute;left:112px;top:140px;font-size:47px;font-weight:400;color:var(--white);white-space:nowrap}
.hero h1 b{font-weight:600}
.hero p{position:absolute;left:112px;top:207px;width:500px;font-size:20px;line-height:35px;color:var(--white);font-weight:300}
.btn{position:absolute;background:var(--red);color:var(--white);font-size:15px;display:flex;align-items:center;justify-content:center;gap:8px;white-space:nowrap}

.features-bg{position:absolute;top:777px;left:0;width:1200px;height:470px;background:linear-gradient(var(--page-tint),#fff)}
.feature{position:absolute;top:694px;height:224px;background:var(--white);box-shadow:0 3px 10px rgba(0,0,0,.12);padding:26px 28px}
.feature h3{margin-top:12px;font-size:21px;font-weight:400}
.feature p{margin-top:14px;font-size:13.5px;line-height:23px;color:var(--ink-soft)}

.about-frame{position:absolute;left:113px;top:1020px;width:426px;height:358px;border:2px solid var(--red)}
.photo{position:absolute}
.section-title{font-size:46px;font-weight:400;white-space:nowrap}
.section-title b{font-weight:600}
.about-text{position:absolute;left:599px;top:1082px;width:490px;font-size:15.5px;line-height:34.3px;color:var(--ink-soft)}

.services-head{position:absolute;top:1490px;left:0;width:1200px;text-align:center;color:var(--teal-ink)}
.services-head p{margin-top:8px;font-size:20px;color:#333}
.card{position:absolute;width:316px;height:235px;border:2px solid var(--line);padding:22px 20px;background:var(--white)}
.card.hot{border-color:#f0a7ac}
.card .ic{width:68px;height:68px;border-radius:50%;background:var(--icon-bg);display:flex;align-items:center;justify-content:center}
.card h3{margin-top:14px;font-size:18.5px;font-weight:400;white-space:nowrap}
.card.hot h3{color:var(--red)}
.card p{margin-top:10px;font-size:13.5px;line-height:23px;color:var(--ink-soft);height:46px;overflow:hidden}
.card .arr{margin-top:4px}

.contact-row{position:absolute;display:flex;gap:20px;align-items:flex-start}
.contact-row .ci{width:48px;height:48px;border-radius:50%;background:#eef1f4;display:flex;align-items:center;justify-content:center;flex:none}
.contact-row .lbl{font-size:19px;color:#333}
.contact-row .val{font-size:20px;color:#333;margin-top:6px;white-space:nowrap}

.footer{position:absolute;top:2770px;left:0;width:1200px;height:392px;background:var(--red);color:var(--white)}
.footer-curve{position:absolute;top:2740px;left:0}
.fcol{position:absolute;top:100px;font-size:15px}
.fcol h4{font-size:16px;font-weight:600;margin-bottom:14px}
.fcol li{list-style:none;line-height:36.5px}
.footer .bottom{position:absolute;top:355px;left:0;width:1200px;border-top:1px solid rgba(255,255,255,.5)}
.footer .bottom span{position:absolute;top:12px;font-size:13.5px}
.involved{display:inline-flex;background:var(--white);color:#333;padding:12px 15px;font-size:15px;margin-top:12px}
.fsoc{width:30px;height:30px;border-radius:50%;background:var(--white);display:inline-block;margin-right:8px}
</style>
</head>
<body>

<div class="topbar">
  <div class="topbar-red"></div>
  <div class="addr">
    <svg width="16" height="18" viewBox="0 0 16 18"><path d="M8 1a6 6 0 0 0-6 6c0 4.5 6 10 6 10s6-5.5 6-10a6 6 0 0 0-6-6z" fill="#fff"/><circle cx="8" cy="7" r="2.3" fill="#d7232f"/></svg>
    48 Larkspur Rd | Aldenvale, SC 29600
  </div>
  <div class="contact">
    <svg width="16" height="16" viewBox="0 0 24 24"><path d="M6.6 10.8a15 15 0 0 0 6.6 6.6l2.2-2.2a1 1 0 0 1 1-.25 11.4 11.4 0 0 0 3.6.57 1 1 0 0 1 1 1V20a1 1 0 0 1-1 1A17 17 0 0 1 3 4a1 1 0 0 1 1-1h3.5a1 1 0 0 1 1 1c0 1.25.2 2.45.57 3.6a1 1 0 0 1-.25 1z" fill="#fff"/></svg>
    <span style="margin-right:14px">555-014-2276</span>
    <span class="dot"></span><span class="dot"></span><span class="dot"></span><span class="dot"></span>
  </div>
</div>

<header class="header">
  <div class="logo" style="left:112px;top:38px;color:#222"><span class="sq"></span>Corvane Systems</div>
  <nav class="nav">
    <a class="active">HOME</a><a>SERVICES ⌄</a><a>ABOUT</a><a>CONTACT</a>
  </nav>
  <a class="quote-btn">REQUEST A QUOTE</a>
</header>

<section class="hero" role="img" aria-label="Engineer working on a laptop inside a data center server aisle">
  <h1><b>Data Center</b> Services</h1>
  <p>We offer colocation, virtualization, storage as a service and disaster recovery out of our own enterprise-grade data center.</p>
  <a class="btn" style="left:114px;top:346px;width:217px;height:47px">EXPLORE OUR SERVICES</a>
</section>

<div class="features-bg"></div>
<div class="feature" style="left:69px;width:325px">
  <svg width="54" height="54" viewBox="0 0 54 54" fill="none" stroke="#333" stroke-width="1.6"><path d="M8 30l10-8 9 5 9-5 10 8-12 12-7-5-7 5z"/><path d="M12 8l2 4 4 .5-3 3 .8 4-3.8-2-3.8 2 .8-4-3-3 4-.5zM27 6l2 4 4 .5-3 3 .8 4-3.8-2-3.8 2 .8-4-3-3 4-.5zM42 8l2 4 4 .5-3 3 .8 4-3.8-2-3.8 2 .8-4-3-3 4-.5z"/></svg>
  <h3>A True Partner</h3>
  <p>One size data center architecture does not fit all.We take the time to understand your specific requirements.</p>
</div>
<div class="feature" style="left:434px;width:333px">
  <svg width="54" height="54" viewBox="0 0 54 54" fill="none" stroke="#333" stroke-width="1.6"><path d="M27 4l19 7v14c0 12-8 20-19 25C16 45 8 37 8 25V11z"/><circle cx="27" cy="27" r="9"/><path d="M23 27l3 3 5-6"/></svg>
  <h3>High Security</h3>
  <p>Our data center is a Tier III, standalone structure designed to withstand wind speeds up to 206mph.</p>
</div>
<div class="feature" style="left:797px;width:333px">
  <svg width="54" height="54" viewBox="0 0 54 54" fill="none" stroke="#333" stroke-width="1.6"><circle cx="27" cy="27" r="17" stroke-dasharray="6 3"/><circle cx="27" cy="27" r="11"/><path d="M21 27l4 4 8-8"/></svg>
  <h3>Availability</h3>
  <p>The facility is powered by two separate utility feeds and a Brennard diesel generator.</p>
</div>

<section class="about">
  <div class="about-frame"></div>
  <div class="photo" style="left:129px;top:1042px;width:431px;height:356px;background:linear-gradient(120deg,#1c3a5e,#3d6b9a 55%,#15314f)" role="img" aria-label="Two technicians reviewing a laptop between server racks"></div>
  <h2 class="section-title abs" style="left:599px;top:1010px"><b>About</b> Us</h2>
  <p class="about-text">Like most great businesses Corvane Systems began in a gargage during the summer of 1995 in Aldenvale, SC. It was a part time venture by Martin Caldwell and his business partner Owen Perrick. They had discovered an opportunity in technology sales and service after a combined 30 years at Halvern Power in information technology. By 2000, the two set out on their own and were working on the venture full-time.</p>
  <a class="btn" style="left:599px;top:1350px;width:218px;height:47px">DISCOVER OUR STORY</a>
</section>

<section>
  <div class="services-head">
    <h2 class="section-title"><b>Our</b> Services</h2>
    <p>Comprehensive IT &amp; MSP Solutions to Power Your Business</p>
  </div>

  <div class="card" style="left:112px;top:1641px">
    <div class="ic"><svg width="34" height="34" viewBox="0 0 34 34" fill="none" stroke="#333" stroke-width="1.5"><rect x="6" y="4" width="18" height="24"/><path d="M10 10h10M10 15h10M10 20h6"/><rect x="18" y="18" width="10" height="10"/></svg></div>
    <h3>Cybersecurity</h3>
    <p>Protect your business with robust cybersecurity solutions. From threat</p>
    <svg class="arr" width="18" height="12" viewBox="0 0 18 12" fill="none" stroke="#333" stroke-width="1.5"><path d="M1 6h15M11 1l5 5-5 5"/></svg>
  </div>
  <div class="card hot" style="left:443px;top:1641px">
    <div style="width:68px;height:68px;display:flex;align-items:center;justify-content:center"><svg width="56" height="56" viewBox="0 0 56 56" fill="none" stroke="#d7232f" stroke-width="1.6"><circle cx="28" cy="30" r="13"/><path d="M15 30h26M28 17v26"/><circle cx="28" cy="8" r="4"/><circle cx="9" cy="20" r="3.5"/><circle cx="47" cy="20" r="3.5"/><circle cx="9" cy="44" r="3.5"/><circle cx="47" cy="44" r="3.5"/></svg></div>
    <h3>Managed Networks for MDUs</h3>
    <p>Reliable Connectivity for Multi-Dwelling Units. Custom-designed network</p>
    <svg class="arr" width="18" height="12" viewBox="0 0 18 12" fill="none" stroke="#d7232f" stroke-width="1.5"><path d="M1 6h15M11 1l5 5-5 5"/></svg>
  </div>
  <div class="card" style="left:774px;top:1641px">
    <div class="ic"><svg width="34" height="34" viewBox="0 0 34 34" fill="none" stroke="#333" stroke-width="1.5"><path d="M8 14a7 7 0 0 1 13-4 6 6 0 0 1 6 8"/><rect x="9" y="14" width="8" height="16"/><rect x="19" y="18" width="8" height="12"/></svg></div>
    <h3>Data Center Services</h3>
    <p>Scalable, Secure, and Always On<br>From rack hosting to full-service data</p>
    <svg class="arr" width="18" height="12" viewBox="0 0 18 12" fill="none" stroke="#333" stroke-width="1.5"><path d="M1 6h15M11 1l5 5-5 5"/></svg>
  </div>
  <div class="card" style="left:114px;top:1897px">
    <div class="ic"><svg width="34" height="34" viewBox="0 0 34 34" fill="none" stroke="#333" stroke-width="1.5"><rect x="7" y="5" width="12" height="24"/><path d="M10 10h6M10 15h6"/><circle cx="24" cy="24" r="5"/></svg></div>
    <h3>Low Voltage Wiring</h3>
    <p>Clean, Code-Compliant Cabling Done Right. We handle structured cabling,</p>
    <svg class="arr" width="18" height="12" viewBox="0 0 18 12" fill="none" stroke="#333" stroke-width="1.5"><path d="M1 6h15M11 1l5 5-5 5"/></svg>
  </div>
  <div class="card" style="left:446px;top:1897px">
    <div class="ic"><svg width="34" height="34" viewBox="0 0 34 34" fill="none" stroke="#333" stroke-width="1.5"><rect x="5" y="6" width="24" height="16"/><path d="M12 28h10M17 22v6"/><circle cx="13" cy="14" r="3"/><path d="M19 12h6M19 16h6"/></svg></div>
    <h3>Office IT Support</h3>
    <p>On-Demand Expertise for Your Team From hardware setup &amp; troubleshooting</p>
    <svg class="arr" width="18" height="12" viewBox="0 0 18 12" fill="none" stroke="#333" stroke-width="1.5"><path d="M1 6h15M11 1l5 5-5 5"/></svg>
  </div>
  <div class="card" style="left:777px;top:1897px">
    <div class="ic"><svg width="34" height="34" viewBox="0 0 34 34" fill="none" stroke="#333" stroke-width="1.5"><circle cx="17" cy="11" r="5"/><path d="M17 3v2M10 6l1.5 1.5M24 6l-1.5 1.5"/><path d="M8 28a5 5 0 0 1 2-9 7 7 0 0 1 13 0 5 5 0 0 1 2 9z"/></svg></div>
    <h3>Cloud Solutions</h3>
    <p>Secure, scalable cloud migration and management. We help you harness the</p>
    <svg class="arr" width="18" height="12" viewBox="0 0 18 12" fill="none" stroke="#333" stroke-width="1.5"><path d="M1 6h15M11 1l5 5-5 5"/></svg>
  </div>

  <a class="btn" style="left:501px;top:2182px;width:191px;height:47px">VIEW ALL SERVICES</a>
</section>

<section>
  <h2 class="section-title abs" style="left:112px;top:2330px"><b>Contact</b> Us</h2>
  <p class="abs" style="left:112px;top:2403px;font-size:19.5px;color:#333">Ready to enhance your IT infrastructure?</p>
  <div class="contact-row" style="left:112px;top:2455px">
    <div class="ci"><svg width="24" height="24" viewBox="0 0 24 24"><path d="M6.6 10.8a15 15 0 0 0 6.6 6.6l2.2-2.2a1 1 0 0 1 1-.25 11.4 11.4 0 0 0 3.6.57 1 1 0 0 1 1 1V20a1 1 0 0 1-1 1A17 17 0 0 1 3 4a1 1 0 0 1 1-1h3.5a1 1 0 0 1 1 1c0 1.25.2 2.45.57 3.6a1 1 0 0 1-.25 1z" fill="#222"/></svg></div>
    <div><div class="lbl">Phone :</div><div class="val">(555) 014-2276</div></div>
  </div>
  <div class="contact-row" style="left:112px;top:2538px">
    <div class="ci"><svg width="20" height="24" viewBox="0 0 16 18"><path d="M8 1a6 6 0 0 0-6 6c0 4.5 6 10 6 10s6-5.5 6-10a6 6 0 0 0-6-6z" fill="#222"/><circle cx="8" cy="7" r="2.3" fill="#eef1f4"/></svg></div>
    <div><div class="lbl">Address :</div><div class="val">48 Larkspur Rd, Aldenvale, SC 29600</div></div>
  </div>
  <a class="btn" style="left:112px;top:2637px;width:185px;height:46px">GET IN TOUCH
    <svg width="18" height="12" viewBox="0 0 18 12" fill="none" stroke="#fff" stroke-width="1.6"><path d="M1 6h15M11 1l5 5-5 5"/></svg></a>
  <div class="photo" style="left:552px;top:2350px;width:538px;height:339px;background:linear-gradient(120deg,#0f2a48,#2e5d8c 50%,#102a44)" role="img" aria-label="Two IT professionals with a laptop discussing in a server room"></div>
</section>

<svg class="footer-curve" width="1200" height="32" viewBox="0 0 1200 32" preserveAspectRatio="none"><path d="M0 32 Q600 0 1200 0 V32 Z" fill="#d7232f"/></svg>
<footer class="footer">
  <div class="logo" style="left:112px;top:88px;color:#fff"><span class="sq" style="background:#fff"></span>Corvane Systems</div>
  <p class="abs" style="left:114px;top:172px;width:270px;font-size:13.5px;line-height:23.5px">Providing managed networks, data center services, and office IT support tailored to your needs.</p>
  <div class="abs" style="left:114px;top:270px"><span class="fsoc"></span><span class="fsoc"></span><span class="fsoc"></span><span class="fsoc"></span></div>

  <div class="fcol" style="left:436px"><h4>QUICK LINKS</h4><ul><li>HOME</li><li>ABOUT US</li><li>SERVICES</li><li>CONTACT US</li></ul></div>
  <div class="fcol" style="left:621px"><h4>SERVICES</h4><ul><li>CYBERSECURITY</li><li>LOW VOLTAGE WIRING</li><li>DATA CENTER SERVICES</li><li>OFFICE IT SUPPORT</li><li>NETWORKS FOR MDU</li></ul></div>
  <div class="fcol" style="left:864px"><h4>CONNECT WITH US</h4>
    <div style="display:flex;gap:10px;align-items:center;line-height:36px"><svg width="24" height="16" viewBox="0 0 24 16"><rect width="24" height="16" rx="2" fill="#fff"/><path d="M1 1l11 8 11-8" fill="none" stroke="#d7232f" stroke-width="1.6"/></svg>support@quorbelna.com</div>
    <div style="display:flex;gap:10px;align-items:center;line-height:36px"><svg width="18" height="18" viewBox="0 0 24 24"><path d="M6.6 10.8a15 15 0 0 0 6.6 6.6l2.2-2.2a1 1 0 0 1 1-.25 11.4 11.4 0 0 0 3.6.57 1 1 0 0 1 1 1V20a1 1 0 0 1-1 1A17 17 0 0 1 3 4a1 1 0 0 1 1-1h3.5a1 1 0 0 1 1 1c0 1.25.2 2.45.57 3.6a1 1 0 0 1-.25 1z" fill="#fff"/></svg>555-014-2276</div>
    <a class="involved">GET INVOLVED</a>
  </div>

  <div class="bottom">
    <span style="left:114px">2025 © Corvane Systems of SC, Inc.</span>
    <span style="left:844px">Terms &amp; Conditions - Privacy policy</span>
  </div>
</footer>

</body>
</html>
```